Online radio: TunaWave homepage redesign

TunaWave is one of the world's leading brands of personalizable online radio -- similar to Melodex, but aimed at a somewhat older audience (age 35-54).

We'd like to redesign our homepage with a more contemporary look: It should emphasize our wide variety of GENRES (as the primary navigation), with the search field easy to find as a secondary navigation.

We'd like to retain our corporate color of maroon/plum. (We are not committed to the gold/yellow secondary color.)

See our current homepage at www.tunawave-example.com and our in-house attempt at an improved design at http://web4.tunawave-example.com/finder/2013ms/.

Ideally, we'd like to see designs for up to THREE different states:

(1) An initial state when users first come to the page.

(2) What the page would look like as the user is looking at channel options.

(3) What the page would look like once the media player is launched.

However, you may be able to combine (2) and (3) in a single screenshot.

Thanks!
Updates

At the request of several designers, we have decided to extend our deadline by four days. At the same time, we have increased our budget, including the addition of a 2nd place award. Thanks for your excellent work!

Thanks very much for your designs! We are very pleased with the overall quality of the work we are seeing. One reminder: As our brief says, the user interface "should emphasize our wide variety of GENRES (as the primary navigation), with the search field easy to find as a secondary navigation," and we feel that your design uses the SEARCH field as the primary navigation. Many of the designs use a large search field as the primary navigation. If yours does, you might want to tweak your design to put a greater emphasis on browsing genres as the primary navigation. Thanks and good luck!

Target Market(s)

Adults age 35-54 listening to online radio at work

Industry/Entity Type

Radio

Font styles to use
Sans Serif

Requirements
Must have
• This is a design/UI project -- we do not need code

```html
<!DOCTYPE html>
<html lang="en">
<head>
<meta charset="utf-8">
<title>TunaWave – Online Radio</title>
<link href="https://fonts.googleapis.com/css2?family=Open+Sans:wght@400;600;700;800&display=swap" rel="stylesheet">
<style>
:root{
  --plum:#5a0046;
  --plum-dark:#4a003a;
  --pink:#e94fd7;
  --gold:#f5c400;
  --ink:#111;
  --item:#3a3a3a;
  --item-top:#1f1f1f;
  --sidebar:#eeeeee;
  --white:#fff;
}
*{box-sizing:border-box;margin:0;padding:0}
html,body{width:1200px;height:886px;overflow:hidden}
body{position:relative;background:#f6f6f6;font-family:"Open Sans",sans-serif;color:var(--white)}
.band-top{position:absolute;left:0;top:0;width:1200px;height:155px;background:var(--plum)}
.band-bottom{position:absolute;left:0;top:784px;width:1200px;height:102px;background:var(--plum);border-top:7px solid var(--ink)}

.brand{position:absolute;left:180px;top:19px;display:flex;align-items:center;gap:6px}
.brand-dot{width:52px;height:52px;border-radius:50%;background:var(--gold)}
.brand-name{font-size:40px;font-weight:700;letter-spacing:-1.5px;color:var(--white);white-space:nowrap}

.site-search{position:absolute;left:478px;top:28px;width:275px;height:36px;border-radius:4px;border:1px solid #b48aa8;background:#9c6b90;display:flex;overflow:hidden}
.site-search span{flex:1;font-size:12px;line-height:34px;color:#3a1a33;padding:0 7px;white-space:nowrap;overflow:hidden}
.site-search i{width:34px;flex:none;background:#7e3d70;display:flex;align-items:center;justify-content:center}
.top-icons{position:absolute;left:770px;top:36px;display:flex;gap:8px}
.round-icon{width:20px;height:20px;border-radius:50%;background:#000;display:flex;align-items:center;justify-content:center;font-size:12px;font-weight:700}
.account{position:absolute;left:838px;top:35px;display:flex;gap:12px;font-size:15.5px;white-space:nowrap}
.account span{display:flex;align-items:center;gap:5px}

.shell{position:absolute;left:179px;top:93px;width:842px;height:734px;background:var(--white);display:flex}
.sidebar{width:227px;height:100%;background:var(--sidebar);padding:14px 0 0 11px}
.artist-search{width:206px;height:34px;border:1px solid #c9c9c9;border-radius:3px;background:#e2e2e2;color:#444;font-size:14.5px;padding:6px 10px;display:flex;justify-content:space-between;align-items:center}
.side-rule{width:206px;height:1px;background:#d4d4d4;margin:12px 0 17px}
.nav{width:203px;margin-left:2px;list-style:none}
.nav li{height:40.5px;background:var(--item);border-bottom:1px solid #555;font-size:14.5px;padding:0 11px;display:flex;align-items:center;justify-content:space-between;white-space:nowrap}
.nav li.lead{background:var(--item-top);height:46px;border-bottom:2px solid #555}
.toggle{width:18px;height:18px;border-radius:50%;background:var(--pink);display:flex;align-items:center;justify-content:center}

.content{flex:1;position:relative}
.hero{height:216px;background:radial-gradient(ellipse at 45% 20%,#6a6a6a 0%,#333 40%,#111 80%);display:flex;align-items:center;justify-content:center}
.hero h1{font-weight:400;font-size:24px;margin-top:-10px;white-space:nowrap}
.hero h1 strong{color:var(--pink);font-weight:700}

.genre{position:absolute;width:147px}
.genre-cap{display:block;width:147px;height:6px}
.genre-art{width:147px;height:149px;background:#111;padding:5px;display:grid;grid-template-columns:1fr 1fr;gap:2px}
.genre-art div{width:100%;height:100%}
.genre-label{width:135px;height:42px;margin-left:6px;background:var(--plum);clip-path:polygon(0 0,100% 0,100% 100%,50% 78%,0 100%);font-weight:700;font-size:14px;text-align:center;padding-top:9px;white-space:nowrap}
</style>
</head>
<body>
<div class="band-top"></div>
<div class="band-bottom"></div>

<header>
  <div class="brand"><span class="brand-dot"></span><span class="brand-name">TunaWave</span></div>
  <div class="site-search"><span>Find radio that plays your favorite music</span><i><svg width="14" height="14" viewBox="0 0 14 14"><circle cx="5.5" cy="5.5" r="4" fill="none" stroke="#fff" stroke-width="2"/><line x1="8.5" y1="8.5" x2="13" y2="13" stroke="#fff" stroke-width="2.2"/></svg></i></div>
  <div class="top-icons">
    <span class="round-icon"><svg width="10" height="10" viewBox="0 0 10 10" fill="#fff"><rect x="0" y="0" width="2.5" height="2.5"/><rect x="3.75" y="0" width="2.5" height="2.5"/><rect x="7.5" y="0" width="2.5" height="2.5"/><rect x="0" y="3.75" width="2.5" height="2.5"/><rect x="3.75" y="3.75" width="2.5" height="2.5"/><rect x="7.5" y="3.75" width="2.5" height="2.5"/><rect x="0" y="7.5" width="2.5" height="2.5"/><rect x="3.75" y="7.5" width="2.5" height="2.5"/><rect x="7.5" y="7.5" width="2.5" height="2.5"/></svg></span>
    <span class="round-icon">?</span>
  </div>
  <div class="account">
    <span><svg width="16" height="16" viewBox="0 0 16 16"><circle cx="8" cy="8" r="8" fill="#fff"/><rect x="5" y="7" width="6" height="5" fill="var(--plum)"/><path d="M6 7V5.5a2 2 0 0 1 4 0V7" fill="none" stroke="var(--plum)" stroke-width="1.4"/></svg>Login</span>
    <span><svg width="16" height="16" viewBox="0 0 16 16"><circle cx="8" cy="8" r="8" fill="#fff"/><circle cx="8" cy="6" r="2.6" fill="var(--plum)"/><path d="M3.5 13a4.5 4 0 0 1 9 0z" fill="var(--plum)"/></svg>Join for Free</span>
  </div>
</header>

<main class="shell">
  <aside class="sidebar">
    <div class="artist-search">Search Artist<svg width="16" height="16" viewBox="0 0 16 16"><circle cx="6" cy="6" r="4.5" fill="none" stroke="#555" stroke-width="1.8"/><line x1="9.5" y1="9.5" x2="15" y2="15" stroke="#555" stroke-width="2.4"/></svg></div>
    <div class="side-rule"></div>
    <ul class="nav">
      <li class="lead">DJ Picks<span class="toggle"><svg width="8" height="8" viewBox="0 0 8 8"><path d="M2 0l5 4-5 4z" fill="#fff"/></svg></span></li>
      <li class="lead">Genres<span class="toggle"><svg width="8" height="8" viewBox="0 0 8 8"><path d="M0 2l4 5 4-5z" fill="#fff"/></svg></span></li>
      <li>Adult Alternative Rock</li>
      <li>Adult Contemporary</li>
      <li>Alt-Country</li>
      <li>Alternative Rock</li>
      <li>Alternative Rock Classics</li>
      <li>Americana</li>
      <li>Artist features</li>
      <li>Bluegrass</li>
      <li>Blues</li>
      <li>Brit Rock</li>
      <li>Broadway</li>
      <li>Cabaret</li>
      <li class="lead">Surprise Me<span class="toggle"><svg width="8" height="8" viewBox="0 0 8 8"><path d="M2 0l5 4-5 4z" fill="#fff"/></svg></span></li>
    </ul>
  </aside>

  <section class="content">
    <div class="hero" role="img" aria-label="Close-up photo of a studio microphone grille in black and white">
      <h1>Thousands of <strong>radio stations</strong> with endless music</h1>
    </div>

    <div class="genre" style="left:41px;top:254px">
      <svg class="genre-cap" viewBox="0 0 147 6"><path d="M6 0H141L147 6H0z" fill="var(--plum)"/></svg>
      <div class="genre-art" role="img" aria-label="Collage of pop hits album covers"><div style="background:linear-gradient(135deg,#f2d000,#222)"></div><div style="background:linear-gradient(135deg,#e04fc0,#2a9fe0)"></div><div style="background:linear-gradient(135deg,#1d5fb0,#e03030)"></div><div style="background:linear-gradient(135deg,#f5b000,#d02f6a)"></div></div>
      <div class="genre-label">Top 40 / Pop Hits</div>
    </div>
    <div class="genre" style="left:232px;top:254px">
      <svg class="genre-cap" viewBox="0 0 147 6"><path d="M6 0H141L147 6H0z" fill="var(--plum)"/></svg>
      <div class="genre-art" role="img" aria-label="Collage of lite hits album covers"><div style="background:linear-gradient(135deg,#6a5a7a,#c8c0b8)"></div><div style="background:linear-gradient(135deg,#7a5a90,#2a1a30)"></div><div style="background:linear-gradient(135deg,#2a2a2a,#8a7a6a)"></div><div style="background:linear-gradient(135deg,#1a2a80,#e0b040)"></div></div>
      <div class="genre-label">Lite Hits</div>
    </div>
    <div class="genre" style="left:423px;top:254px">
      <svg class="genre-cap" viewBox="0 0 147 6"><path d="M6 0H141L147 6H0z" fill="var(--plum)"/></svg>
      <div class="genre-art" role="img" aria-label="Collage of country album covers"><div style="background:linear-gradient(135deg,#e8d8b0,#c0a070)"></div><div style="background:linear-gradient(135deg,#5a4a3a,#b0a090)"></div><div style="background:linear-gradient(135deg,#1d5fb0,#e03030)"></div><div style="background:linear-gradient(135deg,#8aa0b8,#304050)"></div></div>
      <div class="genre-label">Country</div>
    </div>

    <div class="genre" style="left:41px;top:500px">
      <svg class="genre-cap" viewBox="0 0 147 6"><path d="M6 0H141L147 6H0z" fill="var(--plum)"/></svg>
      <div class="genre-art" role="img" aria-label="Collage of classical album covers"><div style="background:linear-gradient(135deg,#2a0a0a,#8a1a1a)"></div><div style="background:linear-gradient(135deg,#b01820,#3a0a0a)"></div><div style="background:linear-gradient(135deg,#f0e8e0,#c04040)"></div><div style="background:linear-gradient(135deg,#1a1a1a,#7a6a5a)"></div></div>
      <div class="genre-label">Classical</div>
    </div>
    <div class="genre" style="left:232px;top:500px">
      <svg class="genre-cap" viewBox="0 0 147 6"><path d="M6 0H141L147 6H0z" fill="var(--plum)"/></svg>
      <div class="genre-art" role="img" aria-label="Collage of classic rock album covers"><div style="background:linear-gradient(135deg,#3a3020,#8a7a5a)"></div><div style="background:linear-gradient(135deg,#1a1000,#d08020)"></div><div style="background:linear-gradient(135deg,#2a3a30,#6a5a40)"></div><div style="background:linear-gradient(135deg,#200000,#e04010)"></div></div>
      <div class="genre-label">Classical Rock</div>
    </div>
    <div class="genre" style="left:423px;top:500px">
      <svg class="genre-cap" viewBox="0 0 147 6"><path d="M6 0H141L147 6H0z" fill="var(--plum)"/></svg>
      <div class="genre-art" role="img" aria-label="Collage of smooth jazz album covers"><div style="background:linear-gradient(135deg,#e0d0a0,#8a6a30)"></div><div style="background:linear-gradient(135deg,#1a1000,#c09030)"></div><div style="background:linear-gradient(135deg,#f0a030,#b01010)"></div><div style="background:linear-gradient(135deg,#e0e0e0,#e05080)"></div></div>
      <div class="genre-label">Smooth Jazz</div>
    </div>
  </section>
</main>

<footer style="position:absolute;left:0;top:837px;width:1200px;text-align:center;font-size:12.5px;line-height:20px">
  <div style="color:var(--pink)">Home&nbsp; | &nbsp;About&nbsp; | &nbsp;Help&nbsp; | &nbsp;Mobile App</div>
  <div>Copyright © 2014 TunaWave. All rights reserved</div>
</footer>
</body>
</html>
```